Photoshop Design Project

Just looking to use some existing element in emails and printed flyers for a lunch menu promo.

I am attaching a menu in progress to reference only the front page design of a chalkboard, chalk fonts, tagline of :Trade the Same Old Plate for Midday Fresh Bites. Its on the front of the menu.

I just want to drop in a photo of each on three separate pieces with description.

THe design should not be a match to the front of the menu, just utilize its elements. the design is not a lead at all, these should remain familiar with the front of the menu, but please use the elements to your design preference.

Ok to submit one layout that we can repeat, or ok to submit three different versions

Must stick with the colors though, they are brand color combo, not exact by color code, but the oranges and the browns need to stay somewhere and in some capacity.
SO menu attached, check out the front cover for inspirations, to go in email sends embedded, and to print as a flyer.

There are also three images attached they are the to be dropped into each piece, with a desciption
Updates

Reason: seems to be too many questions and I wasnt getting anywhere.. To clarify...One Design Piece (one page), three separate items, same peice, however three total. one for each product photo supplied

I moved the deadline back as there were many questions. To clarify, one design piece to be reused for three different products (sandwiches in this case) Same piece, but one for each sandwich.

I posted a file called Artsquare that now has each photo partnered with its title and description

Target Market(s)

hungry people looking for lunch

Industry/Entity Type

Promo

Requirements
Must have
• Attached Menu front page elements, of chalkboard, chalk font existing front colors.

```html
<!DOCTYPE html>
<html lang="en">
<head>
<meta charset="utf-8">
<title>Midday Bistro – Lunch time Promotion</title>
<link rel="stylesheet" href="https://fonts.googleapis.com/css2?family=Cabin+Sketch:wght@400;700&family=Short+Stack&family=Schoolbell&display=swap">
<style>
  :root {
    --brand-orange: #e5673a;
    --brand-orange-light: #f08a5d;
    --brand-orange-deep: #d9522a;
    --chalk-white: #f2efe9;
    --board-dark: #2b2b2a;
    --board-mid: #3a3a38;
    --frame-white: #f7f6f2;
    --photo-wood: #b98a5a;
    --photo-bread: #d7a86a;
  }
  html, body {
    margin: 0;
    padding: 0;
    overflow: hidden;
    background: #ffffff;
  }
  .flyer {
    position: relative;
    width: 856px;
    height: 1200px;
    overflow: hidden;
    background: linear-gradient(180deg, var(--brand-orange-light) 0%, var(--brand-orange) 45%, var(--brand-orange-deep) 100%);
    font-family: "Short Stack", cursive;
  }
  .chalkboard {
    position: absolute;
    inset: 0;
  }
  .brand-name {
    position: absolute;
    left: 232px;
    top: 150px;
    width: 380px;
    margin: 0;
    font-family: "Cabin Sketch", cursive;
    font-weight: 400;
    font-size: 52px;
    line-height: 1;
    color: var(--chalk-white);
    text-align: center;
  }
  .promo-title {
    position: absolute;
    left: 378px;
    top: 232px;
    margin: 0;
    font-family: "Cabin Sketch", cursive;
    font-weight: 700;
    font-size: 60px;
    line-height: 70px;
    color: var(--brand-orange);
  }
  .tagline-stamp {
    position: absolute;
    left: 30px;
    top: 222px;
    width: 252px;
    height: 252px;
  }
  .tagline-stamp svg {
    position: absolute;
    inset: 0;
  }
  .tagline-text {
    position: absolute;
    left: 34px;
    top: 48px;
    width: 184px;
    margin: 0;
    font-family: "Schoolbell", cursive;
    font-size: 27px;
    line-height: 37px;
    color: var(--chalk-white);
    text-align: center;
    transform: rotate(-4deg);
  }
  .product-name {
    position: absolute;
    right: 62px;
    top: 443px;
    margin: 0;
    font-family: "Schoolbell", cursive;
    font-weight: 400;
    font-size: 40px;
    line-height: 50px;
    color: var(--chalk-white);
    text-align: right;
  }
  .product-description {
    position: absolute;
    right: 34px;
    top: 552px;
    width: 380px;
    margin: 0;
    font-family: "Schoolbell", cursive;
    font-size: 27px;
    line-height: 32px;
    color: var(--brand-orange);
    text-align: right;
  }
  .snapshot {
    position: absolute;
    left: 40px;
    top: 560px;
    width: 362px;
    height: 360px;
    background: var(--frame-white);
    box-shadow: 2px 4px 10px rgba(0,0,0,0.45);
    transform: rotate(-3deg);
  }
  .snapshot-photo {
    position: absolute;
    left: 16px;
    top: 16px;
    width: 330px;
    height: 262px;
    background: radial-gradient(ellipse at 40% 50%, var(--photo-bread) 0%, var(--photo-wood) 55%, #6e5238 100%);
  }
  .snapshot-caption {
    position: absolute;
    left: 22px;
    top: 298px;
    margin: 0;
    font-family: "Schoolbell", cursive;
    font-size: 28px;
    color: #1e1e1e;
  }
  .tape {
    position: absolute;
    width: 110px;
    height: 34px;
    background: rgba(160,160,155,0.55);
  }
  .tape--left { left: 0; top: 630px; transform: rotate(-30deg); }
  .tape--top { left: 60px; top: 548px; transform: rotate(-10deg); }
  .occasions {
    position: absolute;
    left: 500px;
    top: 858px;
    margin: 0;
    font-family: "Schoolbell", cursive;
    font-size: 26px;
    line-height: 30px;
    color: var(--chalk-white);
    transform: rotate(7deg);
    transform-origin: left top;
  }
  .occasions .dot {
    display: inline-block;
    width: 9px;
    height: 9px;
    border: 2px solid var(--chalk-white);
    border-radius: 50%;
    margin: 0 8px;
    vertical-align: middle;
  }
  .contact {
    position: absolute;
    left: 0;
    top: 958px;
    width: 856px;
    text-align: center;
    margin: 0;
    font-family: "Schoolbell", cursive;
  }
  .contact-hours,
  .contact-phone {
    display: block;
    font-size: 36px;
    line-height: 40px;
    color: var(--brand-orange);
  }
  .contact-hours .dot {
    display: inline-block;
    width: 10px;
    height: 10px;
    border: 2px solid var(--brand-orange);
    border-radius: 50%;
    margin: 0 10px;
    vertical-align: middle;
  }
  .contact-web {
    display: block;
    margin-top: 4px;
    font-size: 27px;
    line-height: 34px;
    color: var(--chalk-white);
  }
  .contact-venue,
  .contact-address {
    display: block;
    font-size: 22px;
    line-height: 30px;
    color: var(--chalk-white);
  }
</style>
</head>
<body>
<main class="flyer">
  <svg class="chalkboard" width="856" height="1200" viewBox="0 0 856 1200" aria-hidden="true">
    <defs>
      <radialGradient id="boardShade" cx="50%" cy="45%" r="65%">
        <stop offset="0%" stop-color="#3d3d3b"/>
        <stop offset="70%" stop-color="#2e2e2d"/>
        <stop offset="100%" stop-color="#222221"/>
      </radialGradient>
    </defs>
    <path d="M0 150 Q428 40 856 150 L856 1105 Q428 1185 0 1090 Z" fill="url(#boardShade)"/>
  </svg>

  <h1 class="brand-name">Midday Bistro</h1>

  <h2 class="promo-title">Lunch time<br>Promotion</h2>

  <div class="tagline-stamp">
    <svg width="252" height="252" viewBox="0 0 252 252" aria-hidden="true">
      <circle cx="126" cy="126" r="120" fill="none" stroke="var(--brand-orange)" stroke-width="5"/>
      <circle cx="126" cy="126" r="108" fill="none" stroke="var(--brand-orange)" stroke-width="3"/>
    </svg>
    <p class="tagline-text">Trade the Same Old Plate for Midday Fresh Bites</p>
  </div>

  <h3 class="product-name">Bistro BBQ Chicken<br>Sandwich</h3>

  <p class="product-description">Perfectly grilled BBQ<br>Chicken breast,<br>dill yogurt dressing,<br>Garlic spread, micro<br>greens, Radish and Red<br>bell pepper on fresh<br>Focaccia bread</p>

  <div class="tape tape--top" aria-hidden="true"></div>
  <figure class="snapshot" style="margin:0">
    <div class="snapshot-photo" role="img" aria-label="Photo of the BBQ chicken sandwich on focaccia with micro greens, radish and red pepper on a wooden board"></div>
    <figcaption class="snapshot-caption">Chicken...</figcaption>
  </figure>
  <div class="tape tape--left" aria-hidden="true"></div>

  <p class="occasions">Picnics<span class="dot"></span><br>Office<span class="dot"></span>Parties</p>

  <p class="contact">
    <span class="contact-hours">7.30am - 4.30pm<span class="dot"></span>Monday-Friday</span>
    <span class="contact-phone">555-214-3090</span>
    <span class="contact-web">Order online @middaybistro.example</span>
    <span class="contact-venue">The Harbor Court Inn</span>
    <span class="contact-address">1250 Willow Bend Road, Fairview, CA</span>
  </p>
</main>
</body>
</html>
```